One business card required with 2 company logos and 2 people's details

One business card required.
No preference on design - One side could show the 2 different business logos for the companies we own. The reverse could have the details shown below.
Another option could be one business one side and one business on the reverse. Happy to receive designs.

Carol Denbigh
07700 318 274
Rachel Tolland
07700 582 036

website: truelymarvellous.example
email: info@truelymarvellous.example

website: ironwillowevents.example
email: info:ironwillowevents.example

May be nice to have icons instead of the words email/website?

I have included different versions of the logos to help with your design.

Contact Information for Business Card

see project overview

Requirements
Must have
• both company logos, both contact names and contact details

```html
<!DOCTYPE html>
<html lang="en">
<head>
<meta charset="utf-8">
<title>Business Cards – Iron Willow Events &amp; Truely Marvellous</title>
<link rel="stylesheet" href="https://fonts.googleapis.com/css2?family=Montserrat:wght@400;500;700;800&display=swap">
<style>
  :root {
    --page-bg: #2b2b2e;
    --card-bg: #ffffff;
    --willow-blue: #2f6fc2;
    --willow-deep: #23479a;
    --willow-light: #3ec8f0;
    --marvel-navy: #2d2a55;
    --marvel-teal: #2bbcd0;
    --marvel-blue: #2f5fb8;
    --marvel-purple: #8a55b0;
    --text-dark: #222230;
    --divider: #3a78c8;
  }
  * { box-sizing: border-box; margin: 0; padding: 0; }
  html, body {
    width: 1200px; height: 900px; overflow: hidden;
    background: var(--page-bg);
    font-family: "Montserrat", sans-serif;
  }
  .sheet {
    width: 1200px; height: 900px;
    display: flex; flex-direction: column; align-items: center; justify-content: center;
    gap: 36px;
  }
  .card {
    position: relative;
    width: 700px; height: 400px;
    background: var(--card-bg);
    border-radius: 26px;
    overflow: hidden;
    box-shadow: 0 10px 30px rgba(0,0,0,.45);
  }
  .card__swoosh { position: absolute; left: 0; top: 0; width: 700px; height: 400px; }
  .card__brand {
    position: absolute; left: 40px; top: 70px; width: 270px; height: 170px;
    display: flex; align-items: center; justify-content: center; gap: 12px;
    text-align: center;
  }
  .brand__dot { width: 14px; height: 14px; border-radius: 50%; flex: none; }
  .brand__name { font-weight: 700; font-size: 26px; line-height: 1.15; letter-spacing: .5px; }
  .card__divider {
    position: absolute; left: 330px; top: 80px; width: 1.5px; height: 160px;
    background: var(--divider);
  }
  .card__details { position: absolute; left: 360px; top: 88px; color: var(--text-dark); }
  .person__name { font-weight: 800; font-size: 28px; line-height: 1; }
  .person__role { font-size: 17px; font-weight: 500; margin: 4px 0 16px; }
  .contact { list-style: none; }
  .contact__item {
    display: flex; align-items: center; gap: 9px;
    font-size: 16px; line-height: 1.6;
  }
  .contact__icon { width: 14px; height: 14px; flex: none; }

  .card--willow .brand__name, .card--willow .person__name { color: var(--willow-blue); }
  .card--willow .brand__dot { background: var(--willow-blue); }
  .card--willow .contact__icon { fill: var(--willow-deep); }

  .card--marvel .brand__name { color: var(--marvel-navy); }
  .card--marvel .brand__dot { background: var(--marvel-teal); }
  .card--marvel .person__name { color: var(--marvel-navy); text-transform: uppercase; letter-spacing: 1.5px; }
  .card--marvel .contact__icon { fill: var(--marvel-navy); }
</style>
</head>
<body>
<main class="sheet">

  <section class="card card--willow" aria-label="Iron Willow Events business card">
    <svg class="card__swoosh" viewBox="0 0 700 400" aria-hidden="true">
      <defs>
        <linearGradient id="willowBand" x1="0" y1="0" x2="1" y2="0">
          <stop offset="0" stop-color="var(--willow-deep)"/>
          <stop offset=".55" stop-color="#2a7ec0"/>
          <stop offset="1" stop-color="var(--willow-light)"/>
        </linearGradient>
      </defs>
      <path d="M0,262 C180,300 380,340 700,352 L700,400 L0,400 Z" fill="url(#willowBand)"/>
      <path d="M230,318 C400,352 560,362 700,366" fill="none" stroke="#ffffff" stroke-width="3"/>
    </svg>
    <div class="card__brand">
      <span class="brand__dot"></span>
      <span class="brand__name">Iron Willow<br>Events</span>
    </div>
    <div class="card__divider"></div>
    <div class="card__details">
      <h2 class="person__name">Rachel Tolland</h2>
      <p class="person__role">Founder</p>
      <ul class="contact">
        <li class="contact__item"><svg class="contact__icon" viewBox="0 0 16 16"><path d="M3 1h3l1.5 4-2 1.3a9 9 0 0 0 4.2 4.2l1.3-2 4 1.5v3a1.5 1.5 0 0 1-1.5 1.5A13.5 13.5 0 0 1 1.5 2.5 1.5 1.5 0 0 1 3 1z"/></svg>07700 582 036</li>
        <li class="contact__item"><svg class="contact__icon" viewBox="0 0 16 16"><path d="M1 3h14v1.2L8 9 1 4.2z M1 5.8l7 4.8 7-4.8V13H1z"/></svg>info@ironwillowevents.example</li>
        <li class="contact__item"><svg class="contact__icon" viewBox="0 0 16 16"><circle cx="8" cy="8" r="7"/><path d="M1 8h14M8 1c-3 3.5-3 10.5 0 14M8 1c3 3.5 3 10.5 0 14" fill="none" stroke="#fff" stroke-width="1"/></svg>www.ironwillowevents.example</li>
      </ul>
    </div>
  </section>

  <section class="card card--marvel" aria-label="Truely Marvellous business card">
    <svg class="card__swoosh" viewBox="0 0 700 400" aria-hidden="true">
      <defs>
        <linearGradient id="marvelBand" x1="0" y1="0" x2="1" y2="0">
          <stop offset="0" stop-color="var(--marvel-blue)"/>
          <stop offset=".22" stop-color="var(--marvel-teal)"/>
          <stop offset=".6" stop-color="var(--marvel-blue)"/>
          <stop offset="1" stop-color="var(--marvel-purple)"/>
        </linearGradient>
      </defs>
      <path d="M0,255 C180,300 380,345 700,360 L700,400 L0,400 Z" fill="url(#marvelBand)"/>
      <path d="M330,330 C470,352 600,358 700,360 L700,372 C600,368 470,360 330,330 Z" fill="var(--marvel-navy)"/>
      <path d="M330,332 C470,360 600,370 700,374" fill="none" stroke="#ffffff" stroke-width="3"/>
    </svg>
    <div class="card__brand">
      <span class="brand__dot"></span>
      <span class="brand__name">Truely<br>Marvellous</span>
    </div>
    <div class="card__divider"></div>
    <div class="card__details">
      <h2 class="person__name">Carol Denbigh</h2>
      <p class="person__role">Founder</p>
      <ul class="contact">
        <li class="contact__item"><svg class="contact__icon" viewBox="0 0 16 16"><path d="M3 1h3l1.5 4-2 1.3a9 9 0 0 0 4.2 4.2l1.3-2 4 1.5v3a1.5 1.5 0 0 1-1.5 1.5A13.5 13.5 0 0 1 1.5 2.5 1.5 1.5 0 0 1 3 1z"/></svg>07700 318 274</li>
        <li class="contact__item"><svg class="contact__icon" viewBox="0 0 16 16"><path d="M1 3h14v1.2L8 9 1 4.2z M1 5.8l7 4.8 7-4.8V13H1z"/></svg>info@truelymarvellous.example</li>
        <li class="contact__item"><svg class="contact__icon" viewBox="0 0 16 16"><circle cx="8" cy="8" r="7"/><path d="M1 8h14M8 1c-3 3.5-3 10.5 0 14M8 1c3 3.5 3 10.5 0 14" fill="none" stroke="#fff" stroke-width="1"/></svg>www.truelymarvellous.example</li>
      </ul>
    </div>
  </section>

</main>
</body>
</html>
```